Business card for a gourmet fruit and vegetable retail store

Please design a business card for our boutique gourmet fruit and vegetable food store using attached logo design, with the colour options of white, black and lime green. We would like it to be unique and classic, with a large image of the logo on the back of the business card, and the business card details plus a design on the front.

Target Market(s)

High income earners in an affluent Melbourne suburb who value high quality products and done mind paying for it

Industry/Entity Type

Retail

Contact Information for Business Card

Business name: Harwick's Fine Food Merchant
Address: 27 Plumtree Rd, Kelsby VIC 3158
Name: TBC
Position Title: Director
Phone Number: TBC
Mobile: TBC

Business name is: Harwick's Fine Food Merchant. Please allow space for us to fill in the business address, contact number, person's name, position Title and mobile number.

Colors
acd036

Requirements
Must have
• The logo must have our business logo on the back, and our business details and contact details on the front. It must include the colours of white, black and lime green
Nice to have
• It can have different background colours on the front and on the back.
Should not have
• It should not have any other colours aside from white, black and lime green

```html
<!DOCTYPE html>
<html lang="en">
<head>
<meta charset="utf-8">
<title>Harwick's Fine Food Merchant — Business Card Front</title>
<link rel="stylesheet" href="https://fonts.googleapis.com/css2?family=Josefin+Slab:wght@400&display=swap">
<style>
  :root {
    --card-white: #ffffff;
    --ink-black: #111111;
    --pattern-tint: #ececec;
    --lime: #acd036;
  }
  * { margin: 0; padding: 0; box-sizing: border-box; }
  html, body {
    width: 1200px;
    height: 792px;
    overflow: hidden;
    background: var(--card-white);
  }
  .card {
    position: relative;
    width: 1200px;
    height: 792px;
    background: var(--card-white);
    color: var(--ink-black);
    font-family: "Josefin Slab", Georgia, serif;
    overflow: hidden;
  }
  .produce-pattern {
    position: absolute;
    top: 0;
    bottom: 0;
  }
  .produce-pattern--left {
    left: 0;
    width: 380px;
    background: linear-gradient(to right, var(--pattern-tint) 0%, var(--card-white) 100%);
  }
  .produce-pattern--right {
    right: 0;
    width: 260px;
    background: linear-gradient(to left, var(--pattern-tint) 0%, var(--card-white) 100%);
  }
  .brand-mark {
    position: absolute;
    left: 525px;
    top: 70px;
    width: 150px;
    height: 150px;
    border-radius: 50%;
    background: var(--lime);
  }
  .brand {
    position: absolute;
    left: 0;
    right: 0;
    top: 252px;
    text-align: center;
    font-weight: 400;
    color: var(--ink-black);
  }
  .brand-name {
    display: block;
    font-size: 62px;
    line-height: 70px;
    letter-spacing: 0.14em;
    padding-left: 0.14em;
  }
  .brand-tagline {
    display: block;
    margin-top: 4px;
    font-size: 26px;
    line-height: 30px;
    letter-spacing: 0.2em;
    padding-left: 0.2em;
  }
  .contact-details {
    position: absolute;
    left: 0;
    right: 0;
    top: 400px;
    list-style: none;
    text-align: center;
    font-size: 44px;
    line-height: 52px;
    font-weight: 400;
  }
</style>
</head>
<body>
  <main class="card">
    <div class="produce-pattern produce-pattern--left" role="img" aria-label="Faint line-drawn produce pattern along the left side of the card"></div>
    <div class="produce-pattern produce-pattern--right" role="img" aria-label="Faint line-drawn produce pattern along the right side of the card"></div>

    <div class="brand-mark" aria-hidden="true"></div>
    <div class="brand">
      <span class="brand-name">HARWICK'S</span>
      <span class="brand-tagline">FINE FOOD MERCHANT</span>
    </div>

    <ul class="contact-details">
      <li class="business-name">HARWICK'S FINE FOOD MERCHANT</li>
      <li class="address">27 Plumtree Rd, Kelsby VIC 3158</li>
      <li class="person-name">Name:</li>
      <li class="position-title">Position Title: Director</li>
      <li class="phone">Phone Number:</li>
      <li class="mobile">Mobile:</li>
    </ul>
  </main>
</body>
</html>
```